Business Card Design

My husband & I have a singing business so just need a card with my husband's photo on it and our current logo. I have attached the logo on the top of a page plus a photo of my husband & our theme colour we would like is a black background with red writing to match our logo. If you can please also put somewhere on the card "Entertainment for any occasion inc. Pubs, Clubs, Birthday Parties or Weddings". The photo is on the poster attached if you are able to copy it please.

Industry/Entity Type

Business

Contact Information for Business Card

Marty & Jen Ashcroft
Mobile: 0438 926 341
Email: jenna.pruett@mailverge.com

```html
<!DOCTYPE html>
<html lang="en">
<head>
<meta charset="utf-8">
<title>Marty &amp; Jen Ashcroft – Business Card</title>
<link rel="stylesheet" href="https://fonts.googleapis.com/css2?family=Playfair+Display:wght@500;600&family=Archivo+Black&family=Montserrat:wght@400;600;700&display=swap">
<style>
  :root {
    --backdrop: #a9abb5;
    --card-black: #0b0b0b;
    --brand-red: #e8242a;
    --deep-red: #c81e24;
    --text-white: #f4f4f4;
    --photo-dark: #2a1f1b;
    --photo-warm: #7a5040;
  }
  * { margin: 0; padding: 0; box-sizing: border-box; }
  html, body {
    width: 1200px; height: 848px; overflow: hidden;
    background: var(--backdrop);
  }
  .card {
    position: absolute; left: 100px; top: 139px;
    width: 1000px; height: 571px;
    background: var(--card-black);
    overflow: hidden;
    font-family: "Montserrat", sans-serif;
  }
  .card-frame { position: absolute; inset: 0; }
  .brand {
    position: absolute; left: 78px; top: 28px;
    display: flex; align-items: center; gap: 12px;
  }
  .brand-dot {
    width: 22px; height: 22px; border-radius: 50%;
    background: var(--brand-red);
  }
  .brand-name {
    color: var(--brand-red); font-weight: 700;
    font-size: 24px; line-height: 1.05;
  }
  .names {
    position: absolute; left: 92px; top: 132px;
    font-family: "Playfair Display", serif; font-weight: 500;
    font-size: 66px; line-height: 1; color: var(--brand-red);
    letter-spacing: -0.5px;
  }
  .surname {
    position: absolute; left: 262px; top: 222px;
    padding: 4px 18px 2px;
    background: var(--brand-red);
    font-family: "Archivo Black", sans-serif;
    font-size: 30px; letter-spacing: 5px; line-height: 1.1;
    color: var(--card-black);
  }
  .contact { position: absolute; left: 86px; top: 302px; list-style: none; }
  .contact-item {
    display: flex; align-items: center; gap: 10px;
    color: var(--text-white); font-size: 30px; margin-bottom: 26px;
  }
  .contact-icon { width: 34px; height: 34px; flex: none; }
  .tagline {
    position: absolute; left: 74px; top: 438px;
    color: var(--brand-red);
  }
  .tagline-main { font-weight: 700; font-size: 23px; letter-spacing: 0.3px; }
  .tagline-sub { font-weight: 400; font-size: 19px; color: var(--deep-red); margin-top: 2px; }
  .portrait {
    position: absolute; left: 590px; top: 58px;
    width: 390px; height: 513px;
    background: radial-gradient(ellipse at 50% 35%, var(--photo-warm) 0%, var(--photo-dark) 70%);
  }
</style>
</head>
<body>
  <main class="card">
    <svg class="card-frame" width="1000" height="571" viewBox="0 0 1000 571" aria-hidden="true">
      <path d="M60 62 H36 V508 H590 M980 508 V94 H980 M590 94 H980 M540 62 H560" fill="none" stroke="var(--brand-red)" stroke-width="8"/>
      <path d="M36 62 H60" fill="none" stroke="var(--brand-red)" stroke-width="8"/>
    </svg>

    <div class="brand">
      <span class="brand-dot"></span>
      <span class="brand-name">Encore Nights<br>Entertainment</span>
    </div>

    <h1 class="names">Marty &amp; Jen</h1>
    <div class="surname">ASHCROFT</div>

    <ul class="contact">
      <li class="contact-item">
        <svg class="contact-icon" viewBox="0 0 24 24" aria-hidden="true">
          <path fill="var(--brand-red)" d="M6.6 10.8a15.1 15.1 0 0 0 6.6 6.6l2.2-2.2a1 1 0 0 1 1-.25 11.4 11.4 0 0 0 3.6.57 1 1 0 0 1 1 1V20a1 1 0 0 1-1 1A17 17 0 0 1 3 4a1 1 0 0 1 1-1h3.5a1 1 0 0 1 1 1c0 1.25.2 2.45.57 3.57a1 1 0 0 1-.25 1z"/>
        </svg>
        <span>: 0438 926 341</span>
      </li>
      <li class="contact-item">
        <svg class="contact-icon" viewBox="0 0 24 24" aria-hidden="true">
          <rect x="2" y="5" width="20" height="14" fill="var(--brand-red)"/>
          <path d="M2 5 L12 13 L22 5" fill="none" stroke="var(--card-black)" stroke-width="1.6"/>
        </svg>
        <span>: jenna.pruett@mailverge.com</span>
      </li>
    </ul>

    <div class="tagline">
      <p class="tagline-main">ENTERTAINMENT FOR ANY OCCASION</p>
      <p class="tagline-sub">Inc. Pubs, Clubs, Birthday Parties or Weddings</p>
    </div>

    <div class="portrait" role="img" aria-label="Portrait photo of the male singer in a dark patterned shirt"></div>
  </main>
</body>
</html>
```